BRIM Outreach Partners Business Card Rebrand

Hello Designers! We are looking for help designing our new business card to go in conjunction with our company rebrand. Unfortunately, we have an event mid June that requires we get these printed ASAP (before our new website is launched.) We have a mostly complete Brand Book which I have uploaded to this request for your reference to company information, style, fonts. I've also enclosed our logo file in .eps & .jpg. Attached is a sample business card my boss liked but said was "too simple." I made it in Canva and do not profess to be a designer. NOT FOR DESIGN REFERENCE, ONLY FOR CONTEXT Here is what our old website looks like: https://brimoutreachpartners.com/.

```html
<!DOCTYPE html>
<html lang="en">
<head>
<meta charset="utf-8">
<title>BRIM Outreach Partners – Business Card</title>
<link href="https://fonts.googleapis.com/css2?family=Montserrat:wght@400;500;700;800&display=swap" rel="stylesheet">
<style>
  :root {
    --backdrop: #2a2a2c;
    --navy: #03263a;
    --sky: #4fb4e7;
    --white: #ffffff;
    --rule: rgba(255,255,255,0.45);
  }
  * { margin: 0; padding: 0; box-sizing: border-box; }
  html, body { width: 1200px; height: 689px; overflow: hidden; }
  body {
    background: var(--backdrop);
    font-family: "Montserrat", Arial, sans-serif;
    position: relative;
  }
  .card {
    position: absolute;
    top: 190px;
    width: 540px;
    height: 309px;
    border-radius: 22px;
    overflow: hidden;
  }
  .card--front { left: 40px; background: var(--navy); }
  .card--back { left: 620px; background: var(--sky); }

  .brand {
    position: absolute;
    display: flex;
    align-items: center;
  }
  .brand__dot { border-radius: 50%; flex: none; }
  .brand__name {
    font-weight: 800;
    color: var(--white);
    text-transform: uppercase;
    line-height: 1.05;
    letter-spacing: 0.5px;
    white-space: nowrap;
  }

  .card--front .brand { left: 50%; top: 50%; transform: translate(-50%, -50%); gap: 18px; }
  .card--front .brand__dot { width: 86px; height: 86px; background: var(--sky); }
  .card--front .brand__name { font-size: 30px; }

  .card--back .brand { left: 30px; top: 134px; gap: 10px; }
  .card--back .brand__dot { width: 42px; height: 42px; background: var(--white); }
  .card--back .brand__name { font-size: 12.5px; letter-spacing: 0.3px; }

  .divider {
    position: absolute;
    left: 238px; top: 70px;
    width: 1px; height: 170px;
    background: var(--rule);
  }

  .contact {
    position: absolute;
    left: 262px; top: 84px;
    color: var(--white);
    white-space: nowrap;
  }
  .contact__name { font-weight: 800; font-size: 17px; letter-spacing: 0.4px; text-transform: uppercase; }
  .contact__role { font-weight: 500; font-size: 13px; margin-top: 2px; }
  .contact__list { list-style: none; margin-top: 22px; }
  .contact__item {
    display: flex; align-items: center; gap: 9px;
    font-size: 11.5px; font-weight: 500;
    margin-bottom: 9px;
  }
  .contact__icon {
    width: 20px; height: 20px; border-radius: 50%;
    background: var(--white);
    display: flex; align-items: center; justify-content: center;
    flex: none;
  }
  .contact__icon svg { width: 12px; height: 12px; fill: var(--sky); }
</style>
</head>
<body>
  <section class="card card--front" aria-label="Business card front">
    <div class="brand">
      <span class="brand__dot"></span>
      <span class="brand__name">BRIM Outreach<br>Partners</span>
    </div>
  </section>

  <section class="card card--back" aria-label="Business card back">
    <div class="brand">
      <span class="brand__dot"></span>
      <span class="brand__name">BRIM Outreach<br>Partners</span>
    </div>
    <div class="divider"></div>
    <div class="contact">
      <p class="contact__name">Daniel Morrow-Hale</p>
      <p class="contact__role">Managing Partner</p>
      <ul class="contact__list">
        <li class="contact__item">
          <span class="contact__icon"><svg viewBox="0 0 24 24"><path d="M6.6 10.8a15.1 15.1 0 0 0 6.6 6.6l2.2-2.2a1 1 0 0 1 1-.25 11.4 11.4 0 0 0 3.6.57 1 1 0 0 1 1 1V20a1 1 0 0 1-1 1A17 17 0 0 1 3 4a1 1 0 0 1 1-1h3.5a1 1 0 0 1 1 1c0 1.25.2 2.450.57 3.570a1 1 0 0 1-.25 1z"/></svg></span>
          +945-555-0148
        </li>
        <li class="contact__item">
          <span class="contact__icon"><svg viewBox="0 0 24 24"><path d="M2 5h20v14H2z M4 7v.5l8 5.5 8-5.5V7l-8 5.5z" fill-rule="evenodd"/></svg></span>
          daniel@brimoutreachpartners.com
        </li>
        <li class="contact__item">
          <span class="contact__icon"><svg viewBox="0 0 24 24"><path d="M12 2a7 7 0 0 0-7 7c0 5.2 7 13 7 13s7-7.8 7-13a7 7 0 0 0-7-7zm0 9.5A2.5 2.5 0 1 1 12 6.5a2.5 2.5 0 0 1 0 5z"/></svg></span>
          Maplewood, GA based (Central Time)
        </li>
      </ul>
    </div>
  </section>
</body>
</html>
```